Vantor Health Group Presentation Folder, for Cancer Awareness, VERY COLORFUL AND MODERN

Presentation Folder I know pretty much what i want so it should be very eazy , I have included files from folders I use now rebrand them to my new company they will be fine, no sense re creating the wheel
Full Bleed Size
20.87" x 16.68"
53 x 42.4 cm
6260 x 5004 pixels
Document Trim Size
20.75" x 16.56"
52.7 x 42.1 cm
6225 x 4969 pixels
Updates

Low design quality

Industry/Entity Type

Medical

Font styles to use
Serif

Colors

Designer to choose colors to be used in the design.

Requirements
Must have
• really I am not looking for some one to redesign, we like our folder front page and would like to see new word information added., there are two folder front pages to choose from
• So Keep the original front page and redesign the back page and the pockets
• Can Make your Design off of one of the ones I already uploaded
Nice to have
• Keep the same color schemes, Keep the original front page and redesign the back page and the pockets
Should not have
• DO not recreate the front covers, use what I gave you and just rebrand

```html
<!DOCTYPE html>
<html lang="en">
<head>
<meta charset="utf-8">
<title>Vantor Health Group – Presentation Folder Dieline</title>
<link href="https://fonts.googleapis.com/css2?family=Open+Sans:wght@400;600;700&family=Raleway:wght@400;500;600;700&display=swap" rel="stylesheet">
<style>
  :root{
    --stage:#6a6a6a;
    --paper:#ffffff;
    --navy:#0b1f5c;
    --lime:#7cc142;
    --pink:#f296a6;
    --slate:#6d6e71;
    --cyan:#8fd3ea;
    --cut:#e0463f;
    --fold:#5cc08a;
    --ink:#2b2b2b;
  }
  *{box-sizing:border-box;margin:0;padding:0}
  html,body{width:1114px;height:1200px;overflow:hidden;background:var(--stage)}
  .canvas{position:relative;width:1114px;height:1200px;font-family:"Open Sans",sans-serif}
  .dieline{position:absolute;left:0;top:0}

  /* inner spread */
  .band{position:absolute;left:557px;width:500px;color:#fff;font-family:"Raleway",sans-serif}
  .band--title{top:87px;height:37px;background:var(--pink);display:flex;align-items:center;padding-left:40px;font-size:21px;font-weight:600;letter-spacing:2.2px}
  .band--tag{top:538px;height:31px;background:var(--slate);display:flex;align-items:center;padding-left:117px;font-size:16px;font-weight:500;letter-spacing:.3px}
  .gatekeepers{position:absolute;left:573px;width:431px;top:135px;text-align:center;font-family:"Raleway",sans-serif;font-size:14px;font-weight:500;color:#111}
  .obligation{position:absolute;left:605px;width:370px;top:161px;text-align:center;font-family:"Raleway",sans-serif;font-size:11px;line-height:13px;color:#555}
  .photo{position:absolute;box-shadow:4px 6px 10px rgba(0,0,0,.35)}
  .photo--beach{left:127px;top:160px;width:396px;height:255px;transform:rotate(-4deg);background:linear-gradient(180deg,#2f8fe0 0%,#7cc3f2 55%,#e6dccb 72%,#d9cdb5 100%)}
  .photo--table{left:606px;top:254px;width:380px;height:256px;transform:rotate(-4deg);background:linear-gradient(160deg,#e9ecee 0%,#c9b8a2 45%,#a8876a 100%)}
  .ribbon{position:absolute;width:30px;height:66px;border-radius:14px;background:linear-gradient(160deg,#e37ad6,#5fb8ea)}
  .ribbon--left{left:466px;top:106px;transform:rotate(-12deg)}
  .ribbon--right{left:948px;top:193px;transform:rotate(-12deg)}
  .mark-dot{position:absolute;left:617px;top:549px;width:40px;height:40px;border-radius:50%;background:#fff;border:3px solid var(--navy)}
  .intro{position:absolute;left:151px;top:466px;width:360px;font-size:10px;line-height:13px;color:var(--ink)}
  .intro strong{color:var(--navy)}
  .intro-call{position:absolute;left:151px;top:539px;width:370px;font-size:10.5px;line-height:14px;font-weight:600;color:var(--navy)}

  /* pockets */
  .pocket{position:absolute;width:458px;height:218px}
  .pocket svg{position:absolute;left:0;top:0}
  .pocket--flip{transform:rotate(180deg)}
  .pocket--lower-left{left:99px;top:913px}
  .pocket--lower-right{left:561px;top:913px}
  .pocket--upper-left{left:95px;top:630px}
  .pocket--upper-right{left:561px;top:630px}
  .pocket-copy{position:absolute;left:62px;top:38px;width:318px;color:#fff}
  .pocket-copy .lead{font-size:6px;line-height:8.3px;font-weight:700}
  .pocket-copy .body{margin-top:8px;font-size:5.6px;line-height:8px}
  .pocket-copy .headline{margin-top:8px;font-size:13.5px;line-height:18px;font-weight:700}
  .pocket-copy .headline span{color:var(--lime)}
  .brand-lockup{position:absolute;left:150px;top:85px;display:flex;align-items:center;gap:6px}
  .brand-lockup .dot{width:38px;height:38px;border-radius:50%;border:3px solid var(--navy)}
  .brand-lockup .name{font-family:"Raleway",sans-serif;font-size:12px;line-height:13px;font-weight:700;color:var(--navy);width:64px}
  .brand-name{position:absolute;left:0;width:458px;top:157px;text-align:center;font-family:"Raleway",sans-serif;font-size:20px;font-weight:700;color:var(--navy)}
  .brand-division{position:absolute;left:0;width:458px;top:183px;text-align:center;font-size:8px;color:#333}
</style>
</head>
<body>
<div class="canvas">
  <svg class="dieline" width="1114" height="1200" viewBox="0 0 1114 1200" aria-hidden="true">
    <defs>
      <filter id="lift" x="-5%" y="-5%" width="110%" height="115%">
        <feDropShadow dx="2" dy="3" stdDeviation="3" flood-opacity=".35"/>
      </filter>
    </defs>
    <path filter="url(#lift)" d="M58,51 H1056 V403 A13,13 0 0 0 1056,429 V630 H58 V429 A13,13 0 0 0 58,403 Z" fill="#fff" stroke="var(--cut)" stroke-width="1"/>
    <line x1="557" y1="53" x2="557" y2="628" stroke="var(--fold)" stroke-width="1" stroke-dasharray="3 3"/>
    <rect x="111" y="66" width="431" height="548" fill="none" stroke="var(--cyan)" stroke-width="1"/>
    <rect x="573" y="66" width="431" height="548" fill="none" stroke="var(--cyan)" stroke-width="1"/>
  </svg>

  <div class="band band--title">HEREDITARY CANCER SCREENING</div>
  <p class="gatekeepers">Doctors are the Gatekeepers to Genetic Testing.</p>
  <p class="obligation">We have an obligation to help patients understand genetic risk and how testing can guide heath care decisions.</p>

  <div class="photo photo--beach" role="img" aria-label="Photo of a multi-generation family walking hand in hand on a sunny beach"></div>
  <div class="ribbon ribbon--left" role="img" aria-label="Pink and blue awareness ribbon"></div>
  <div class="photo photo--table" role="img" aria-label="Photo of a family sharing a meal at an outdoor table"></div>
  <div class="ribbon ribbon--right" role="img" aria-label="Pink and blue awareness ribbon"></div>

  <div class="band band--tag">The test you order FOR your patients</div>
  <div class="mark-dot"></div>

  <p class="intro"><strong>Hereditary cancer screening</strong> provides vital information to help people with a strong personal or family history of cancer understand their own risk of developing the disease. With this information, they can take steps to Potentially Prevent Cancer, Delay the Onset of Cancer or Catch it at an Earlier stage when outcomes and survival rates are Better.</p>
  <p class="intro-call">Don't be Afraid of the Answer: Knowledge is Power and Power Eradicates Fear. When You are Fearless, You Will Make all the Right Choices!</p>

  <!-- pocket: white brand pocket -->
  <div class="pocket pocket--lower-right">
    <svg width="458" height="218" viewBox="0 0 458 218" aria-hidden="true">
      <path filter="url(#lift)" d="M0,218 L14,22 Q17,0 39,0 H457 V218 Z" fill="#fff" stroke="var(--cut)" stroke-width="1"/>
      <path d="M34,201 L44,35 Q47,15 67,15 H429 V201 Z" fill="none" stroke="var(--cyan)" stroke-width="1"/>
      <g stroke="var(--cut)" stroke-width="1">
        <line x1="172" y1="51" x2="142" y2="81"/><line x1="287" y1="51" x2="317" y2="81"/>
        <line x1="142" y1="120" x2="172" y2="150"/><line x1="317" y1="120" x2="287" y2="150"/>
      </g>
    </svg>
    <div class="brand-lockup"><span class="dot"></span><span class="name">Vantor Health Group</span></div>
    <p class="brand-name">Vantor Health Group</p>
    <p class="brand-division">a division of Meridian Clinical Sales LLC</p>
  </div>

  <!-- pocket: navy message pocket -->
  <div class="pocket pocket--lower-left">
    <svg width="458" height="218" viewBox="0 0 458 218" aria-hidden="true">
      <path filter="url(#lift)" d="M0,218 V0 H421 Q446,0 449,22 L458,218 Z" fill="var(--navy)" stroke="var(--cut)" stroke-width="1"/>
      <path d="M38,15 H406 Q421,15 424,32 L432,201 H38 Z" fill="none" stroke="var(--cyan)" stroke-width="1"/>
    </svg>
    <div class="pocket-copy">
      <p class="lead">There are many benefits to getting tested, regardless of the eventual result. If one of your family members — however distant — had cancer, there is a chance that you inherited a gene mutation that not only increases your personal risk of cancer, but also could be passed to the next generation. Those who are carriers of hereditary cancer gene mutations, could be at risk of getting cancer earlier in life than the general population. The sooner genetic testing is done, the more likely it is that the risk can be managed appropriately.</p>
      <p class="body">Hereditary cancer screening provides vital information to help people with a strong personal or family history of cancer understand their own risk of developing the disease. With this information, they can take steps to Potentially Prevent Cancer, Delay the Onset of Cancer or Catch it at an Earlier stage when outcomes and survival rates are Better.</p>
      <p class="headline">Identifying an inherited genetic mutation has the potential to prevent cancer <span>and save lives.</span></p>
    </div>
  </div>

  <!-- upper pockets: same pieces printed upside down -->
  <div class="pocket pocket--upper-left pocket--flip">
    <svg width="458" height="218" viewBox="0 0 458 218" aria-hidden="true">
      <path filter="url(#lift)" d="M0,218 L14,22 Q17,0 39,0 H457 V218 Z" fill="#fff" stroke="var(--cut)" stroke-width="1"/>
      <path d="M34,201 L44,35 Q47,15 67,15 H429 V201 Z" fill="none" stroke="var(--cyan)" stroke-width="1"/>
      <g stroke="var(--cut)" stroke-width="1">
        <line x1="172" y1="51" x2="142" y2="81"/><line x1="287" y1="51" x2="317" y2="81"/>
        <line x1="142" y1="120" x2="172" y2="150"/><line x1="317" y1="120" x2="287" y2="150"/>
      </g>
    </svg>
    <div class="brand-lockup"><span class="dot"></span><span class="name">Vantor Health Group</span></div>
    <p class="brand-name">Vantor Health Group</p>
    <p class="brand-division">a division of Meridian Clinical Sales LLC</p>
  </div>

  <div class="pocket pocket--upper-right pocket--flip">
    <svg width="458" height="218" viewBox="0 0 458 218" aria-hidden="true">
      <path filter="url(#lift)" d="M0,218 V0 H421 Q446,0 449,22 L458,218 Z" fill="var(--navy)" stroke="var(--cut)" stroke-width="1"/>
      <path d="M38,15 H406 Q421,15 424,32 L432,201 H38 Z" fill="none" stroke="var(--cyan)" stroke-width="1"/>
    </svg>
    <div class="pocket-copy">
      <p class="lead">There are many benefits to getting tested, regardless of the eventual result. If one of your family members — however distant — had cancer, there is a chance that you inherited a gene mutation that not only increases your personal risk of cancer, but also could be passed to the next generation. Those who are carriers of hereditary cancer gene mutations, could be at risk of getting cancer earlier in life than the general population. The sooner genetic testing is done, the more likely it is that the risk can be managed appropriately.</p>
      <p class="body">Hereditary cancer screening provides vital information to help people with a strong personal or family history of cancer understand their own risk of developing the disease. With this information, they can take steps to Potentially Prevent Cancer, Delay the Onset of Cancer or Catch it at an Earlier stage when outcomes and survival rates are Better.</p>
      <p class="headline">Identifying an inherited genetic mutation has the potential to prevent cancer <span>and save lives.</span></p>
    </div>
  </div>
</div>
</body>
</html>
```